Billboard design for retail kitchen cabinet business

We have a large 7,000 square-foot showroom of beautiful kitchen cabinet displays of all different designs and price ranges. In business for over 50 years with expert designers.
Full size Norvale Media 14' X 48' billboard
Target Market(s)
Retail public on high traffic Los Angeles streets

```html
<!DOCTYPE html>
<html lang="en">
<head>
<meta charset="utf-8">
<title>The Cabinet House – Billboard</title>
<link rel="stylesheet" href="https://fonts.googleapis.com/css2?family=Barlow+Condensed:wght@300;600;700&display=swap">
<style>
  :root {
    --page-bg: #b3b3b3;
    --board-light: #f7f7f7;
    --board-mid: #ececec;
    --accent-yellow: #fbb515;
    --band-gray: #8c8c8c;
    --ink: #1f1f1f;
    --white: #ffffff;
  }
  html, body {
    margin: 0;
    width: 1024px;
    height: 1200px;
    overflow: hidden;
    background: var(--page-bg);
  }
  .billboard {
    position: absolute;
    left: 32px;
    top: 460px;
    width: 960px;
    height: 280px;
    box-shadow: 10px 14px 14px rgba(0, 0, 0, 0.45);
  }
  .billboard svg { display: block; width: 100%; height: 100%; }
  .headline {
    font-family: "Barlow Condensed", sans-serif;
    font-weight: 300;
    font-size: 50px;
    fill: var(--ink);
  }
  .headline .highlight { font-weight: 700; fill: var(--accent-yellow); }
  .store-name {
    font-family: "Barlow Condensed", sans-serif;
    font-weight: 700;
    font-size: 80px;
    fill: var(--accent-yellow);
  }
  .phone-number {
    font-family: "Barlow Condensed", sans-serif;
    font-weight: 600;
    font-size: 64px;
    fill: var(--white);
    letter-spacing: -1px;
  }
  .web-address {
    font-family: "Barlow Condensed", sans-serif;
    font-weight: 600;
    font-size: 26px;
    fill: var(--white);
  }
</style>
</head>
<body>
<div class="billboard">
  <svg viewBox="0 0 1586 462" xmlns="http://www.w3.org/2000/svg">
    <defs>
      <linearGradient id="boardGradient" x1="0" y1="0" x2="1" y2="1">
        <stop offset="0" stop-color="var(--board-light)"/>
        <stop offset="1" stop-color="var(--board-mid)"/>
      </linearGradient>
      <linearGradient id="kitchenWarm" x1="0" y1="0" x2="0" y2="1">
        <stop offset="0" stop-color="#f1efea"/>
        <stop offset="0.55" stop-color="#e6dcc6"/>
        <stop offset="1" stop-color="#c8a470"/>
      </linearGradient>
      <linearGradient id="kitchenTaupe" x1="0" y1="0" x2="0" y2="1">
        <stop offset="0" stop-color="#cdbfb6"/>
        <stop offset="1" stop-color="#6e5548"/>
      </linearGradient>
      <linearGradient id="kitchenBright" x1="0" y1="0" x2="0" y2="1">
        <stop offset="0" stop-color="#e4e1dc"/>
        <stop offset="0.5" stop-color="#f3f3f2"/>
        <stop offset="1" stop-color="#d9d6d2"/>
      </linearGradient>
    </defs>

    <rect class="board-bg" width="1586" height="462" fill="url(#boardGradient)"/>

    <!-- photo collage -->
    <polygon class="photo photo-dining" role="img" aria-label="Photo of a bright white kitchen with open shelving and a dining table"
      points="622,140 735,0 1215,0 1250,130 1030,462 760,462 700,380"
      fill="url(#kitchenWarm)" stroke="var(--white)" stroke-width="8" stroke-linejoin="round"/>
    <polygon class="photo photo-taupe" role="img" aria-label="Photo of a taupe kitchen with a dark wood island and bar stools"
      points="855,208 1020,372 925,462 760,462 690,380"
      fill="url(#kitchenTaupe)" stroke="var(--white)" stroke-width="8" stroke-linejoin="round"/>
    <polygon class="photo photo-island" role="img" aria-label="Photo of a modern white kitchen with a marble island and large windows"
      points="1330,0 1586,0 1586,235 1362,462 1045,462 1250,132 1225,98"
      fill="url(#kitchenBright)" stroke="var(--white)" stroke-width="8" stroke-linejoin="round"/>

    <polygon class="accent-triangle" points="1125,0 1312,0 1218,96" fill="var(--accent-yellow)"/>
    <polygon class="corner-band" points="1586,262 1586,462 1408,462" fill="var(--band-gray)"/>

    <!-- contact bands -->
    <polygon class="phone-band" points="0,345 300,345 368,462 0,462" fill="var(--band-gray)"/>
    <polygon class="web-band" points="335,388 690,388 754,462 378,462" fill="var(--accent-yellow)"/>

    <!-- phone icon -->
    <g class="phone-icon" transform="translate(152 352)">
      <rect x="-22" y="-22" width="44" height="44" rx="5" transform="rotate(45)" fill="var(--accent-yellow)" stroke="var(--white)" stroke-width="4"/>
      <path d="M-9,-10 l5,-3 l5,7 l-3,3 c2,4 4,6 8,8 l3,-3 l7,5 l-3,5 c-12,0 -22,-10 -22,-22 z" fill="var(--white)"/>
    </g>

    <text class="phone-number" x="22" y="445">310.555.0142</text>

    <!-- web address -->
    <g class="globe-icon" transform="translate(383 427)" fill="none" stroke="var(--white)" stroke-width="2">
      <circle r="9"/>
      <ellipse rx="4" ry="9"/>
      <line x1="-9" y1="0" x2="9" y2="0"/>
    </g>
    <text class="web-address" x="403" y="436">WWW.THECABINETHOUSE.NET</text>

    <!-- headline -->
    <text class="headline" x="42" y="64">FROM <tspan class="highlight">TRADITIONAL DESIGNS</tspan></text>
    <text class="headline" x="42" y="117">TO THE <tspan class="highlight">LATEST LOOKS</tspan> AND</text>
    <text class="headline" x="42" y="170">
      <tspan class="highlight">STYLES</tspan> YOU WILL FIND</text>
    <text class="headline" x="42" y="222">EXACTLY WHAT YOU WANT AT</text>
    <text class="store-name" x="42" y="298">THE CABINET HOUSE</text>
  </svg>
</div>
</body>
</html>
```